8X8 Realtor Training Expo Flyer

BRAVO SUMMIT REALTY & HALCYON REALTY VENTURES
INVITE ALL TO OUR
LIVE REALTOR TRAINING EXPO

WITH TRAINER / SPEAKER MR. GORDON ALAPATI
SATURDAY AUGUST 13th
9 AM - 1 PM
AT THE MARWICK LODGE
4817 HOLLOWAY CREEK DRIVE
GREENBELT, MD 20770

RSVP PREFERRED BY EMAILING FRONTDESK@BRAVOSUMMITREALTY.COM

```html
<!DOCTYPE html>
<html lang="en">
<head>
<meta charset="utf-8">
<title>Live Realtor Training Expo Flyer</title>
<link href="https://fonts.googleapis.com/css2?family=Dancing+Script:wght@500&family=Montserrat:wght@400;500;600;700;900&display=swap" rel="stylesheet">
<style>
  :root {
    --page-bg: #d9d9d9;
    --paper: #ffffff;
    --teal: #0a8a98;
    --teal-deep: #06606c;
    --teal-light: #12a3b3;
    --band: rgba(3, 60, 70, 0.55);
    --ink: #1f1f1f;
    --bar: #222222;
    --white: #ffffff;
  }
  * { box-sizing: border-box; margin: 0; padding: 0; }
  html, body {
    width: 790px; height: 1200px; overflow: hidden;
    background: var(--page-bg);
    font-family: "Montserrat", Arial, sans-serif;
  }
  .flyer {
    position: absolute; left: 25px; top: 77px;
    width: 740px; height: 1045px;
    background: var(--paper);
    box-shadow: 6px 10px 18px rgba(0,0,0,0.25);
    overflow: hidden;
  }
  .header {
    height: 141px;
    display: flex; justify-content: center; align-items: center; gap: 54px;
  }
  .brand {
    display: flex; align-items: center; gap: 8px;
    color: var(--teal); font-weight: 700; font-size: 15px; letter-spacing: 0.5px;
  }
  .brand-square { width: 16px; height: 16px; background: var(--teal); }
  .panel {
    position: absolute; left: 0; top: 141px; width: 740px; height: 830px;
    background: linear-gradient(180deg, var(--teal) 0%, #088594 55%, #0d95a4 82%, var(--teal) 100%);
    color: var(--white); text-align: center;
  }
  .panel > * { position: absolute; left: 0; width: 100%; }
  .wave-texture {
    top: 560px; height: 270px;
    background:
      radial-gradient(ellipse 70% 45% at 20% 75%, rgba(30, 190, 205, 0.45), transparent 70%),
      radial-gradient(ellipse 60% 40% at 85% 60%, rgba(25, 175, 190, 0.3), transparent 70%);
  }
  .invite {
    top: 50px; display: flex; justify-content: center; align-items: center; gap: 20px;
    font-family: "Dancing Script", cursive; font-size: 50px; font-weight: 500;
  }
  .swash {
    display: block; width: 76px; height: 12px; border-radius: 6px;
    background: linear-gradient(90deg, rgba(255,255,255,0.15), rgba(255,255,255,0.55), rgba(255,255,255,0.15));
  }
  .event-type { top: 124px; font-size: 43px; font-weight: 600; letter-spacing: 0.5px; }
  .expo-word { top: 186px; left: 50%; width: 580px; margin-left: -290px; height: 170px; }
  .date { top: 396px; font-size: 42px; font-weight: 700; }
  .time { top: 448px; font-size: 27px; font-weight: 500; }
  .speaker-band {
    top: 516px; height: 95px;
    background: linear-gradient(90deg, transparent 10%, var(--band) 30%, var(--band) 70%, transparent 90%);
  }
  .speaker-role { top: 533px; font-size: 21px; font-weight: 500; }
  .speaker-name { top: 557px; font-size: 34px; font-weight: 700; }
  .venue { top: 652px; font-size: 32px; font-weight: 400; }
  .venue strong { font-weight: 700; }
  .address { top: 704px; font-size: 21px; line-height: 27px; font-weight: 400; }
  .rsvp-bar { top: 777px; height: 53px; }
  .rsvp-text { top: 790px; font-size: 21px; font-weight: 500; letter-spacing: 0.2px; }
  .rsvp-text strong { font-weight: 700; }
  .footer-url {
    position: absolute; left: 0; top: 971px; width: 100%; height: 74px;
    display: flex; align-items: center; justify-content: center;
    font-size: 28px; font-weight: 500; color: var(--ink);
  }
  .footer-url .domain { color: var(--teal); }
</style>
</head>
<body>
  <main class="flyer">
    <header class="header">
      <div class="brand"><span class="brand-square"></span>BRAVO SUMMIT REALTY</div>
      <div class="brand"><span class="brand-square"></span>HALCYON REALTY VENTURES</div>
    </header>

    <section class="panel">
      <div class="wave-texture" role="img" aria-label="Soft flowing wave texture in light teal"></div>
      <div class="invite">
        <span class="swash" role="img" aria-label="Decorative swash ornament"></span>
        <span>Invite all to our</span>
        <span class="swash" role="img" aria-label="Decorative swash ornament"></span>
      </div>
      <h1 class="event-type">LIVE REALTOR TRAINING</h1>
      <svg class="expo-word" viewBox="0 0 580 170" aria-label="EXPO">
        <defs>
          <linearGradient id="chrome" x1="0" y1="0" x2="0" y2="1">
            <stop offset="0" stop-color="#ffffff"/>
            <stop offset="0.45" stop-color="#c9c9c9"/>
            <stop offset="0.55" stop-color="#8e8e8e"/>
            <stop offset="1" stop-color="#f2f2f2"/>
          </linearGradient>
        </defs>
        <text x="290" y="158" text-anchor="middle" font-family="Montserrat, Arial, sans-serif" font-weight="900" font-size="196" letter-spacing="-14" fill="#064e58" transform="translate(6 6)">EXPO</text>
        <text x="290" y="158" text-anchor="middle" font-family="Montserrat, Arial, sans-serif" font-weight="900" font-size="196" letter-spacing="-14" fill="url(#chrome)" stroke="#111" stroke-width="5" paint-order="stroke">EXPO</text>
      </svg>
      <p class="date">SATURDAY, AUGUST 13TH</p>
      <p class="time">AT 9 AM - 1 PM</p>
      <div class="speaker-band"></div>
      <p class="speaker-role">WITH TRAINER / SPEAKER</p>
      <p class="speaker-name">MR. GORDON ALAPATI</p>
      <p class="venue">AT <strong>THE MARWICK LODGE</strong></p>
      <p class="address">4817 Holloway Creek Drive<br>Greenbelt, MD 20770</p>
      <svg class="rsvp-bar" viewBox="0 0 740 53" preserveAspectRatio="none">
        <path d="M58 53 L100 6 Q106 0 114 0 L626 0 Q634 0 640 6 L682 53 Z" fill="var(--bar)"/>
      </svg>
      <p class="rsvp-text">RSVP: <strong>FRONTDESK@BRAVOSUMMITREALTY.COM</strong></p>
    </section>

    <footer class="footer-url">www.<span class="domain">bravosummitrealty</span>.com</footer>
  </main>
</body>
</html>
```